New young doctors office business card

Doctor's office
Hello:
My name is Dr. Mateo Anselmo Quiroga Benítez. I need a business card for my new office located within a hospital. The name of the hospital is "Hospital Almendral". Although the hospital logo and name must be included in the business card, please make me a personal logo for myself. The logo might be maybe my name in a stylish font, or my initials (MAQB) or something like that. Im more inclined to a font logo, rather than a image logo, but a good one might change my mind. The info on my business card is going to be in spanish. The following info must be included please (the info within parenthesis is not to be included, it is provided for you to understand it since it's in spanish, so you can properly place it on the card):
-Dr. Mateo Anselmo Quiroga Benítez (my name)
-Medicina general (My specialty)
-Hospital Almendral (The name of the hospital where my office is)
-Calle Tomás Ibarrola #527 Col. Peñascal (address)
-Tel 471-5836 (Office phone)
-Sábado y domingo 10:00 am a 10:00pm (Office hours)
-Emergencias: 613-907-5148 (Emergency phone)
-mateoqb@correoandino.net (email)
-English Spoken
So, that's all the info i need to be on the business card. Although it's a business card for a doctor's office, i dont want it to be a boring, plain business card. Make it eye-catchy and stylish please. As i said, the hospital logo must be included. You'll find it on the heading of the PDF file i attached, but dont make it the center of attention.
Physician
Hello:My name is Dr. Mateo Anselmo Quiroga Benítez. I need a business card for my new office located within a hospital. The name of the hospital is "Hospital Almendral". Although the hospital logo and name must be included in the business card, please make me a personal logo for myself. The logo might be maybe my name in a stylish font, or my initials (MAQB) or something like that. Im more inclined to a font logo, rather than a image logo, but a good one might change my mind. The info on my business card is going to be in spanish. The following info must be included please (the info within parenthesis is not to be included, it is provided for you to understand it since it's in spanish, so you can properly place it on the card):-Dr. Mateo Anselmo Quiroga Benítez (my name)-Medicina general (My specialty)-Hospital Almendral (The name of the hospital where my office is)-Calle Tomás Ibarrola #527 Col. Peñascal (address)-Tel 471-5836 (Office phone)-Sábado y domingo 10:00 am a 10:00pm (Office hours)-Emergencias: 613-907-5148 (Emergency phone)-mateoqb@correoandino.net (email)-English Spoken So, that's all the info i need to be on the business card. Although it's a business card for a doctor's office, i dont want it to be a boring, plain business card. Make it eye-catchy and stylish please. As i said, the hospital logo must be included. You'll find it on the heading of the PDF file i attached, but dont make it the center of attention.

```html
<!DOCTYPE html>
<html lang="es">
<head>
<meta charset="utf-8">
<title>Tarjeta de presentación — Dr. Mateo Anselmo Quiroga Benítez</title>
<link rel="stylesheet" href="https://fonts.googleapis.com/css2?family=Lato:wght@400;700&display=swap">
<style>
  :root {
    --backdrop: #e6e7ea;
    --brand-blue: #0b3a8e;
    --strip-blue: #09337e;
    --frame-blue: #0d43a2;
    --paper: #ffffff;
    --ink-gray: #4a4a4a;
    --rule-gray: #8a8a8a;
  }
  * { box-sizing: border-box; margin: 0; padding: 0; }
  html, body {
    width: 1200px; height: 782px; overflow: hidden;
    background: var(--backdrop);
    font-family: "Lato", "Helvetica Neue", Arial, sans-serif;
  }
  .canvas {
    position: relative; width: 1200px; height: 782px;
    display: flex; align-items: center; justify-content: center; gap: 40px;
  }
  .card {
    position: relative; width: 540px; height: 310px; overflow: hidden;
    box-shadow: 0 6px 18px rgba(0,0,0,.18);
  }
  .film-strip {
    position: absolute; top: 0; bottom: 0; width: 52px;
    display: flex; flex-direction: column; justify-content: space-around; align-items: center;
    padding: 14px 0;
  }
  .film-strip--left { left: 0; }
  .film-strip--right { right: 0; }
  .film-hole { width: 30px; height: 24px; }

  /* Front */
  .card--front { background: var(--brand-blue); }
  .card--front .film-strip { background: var(--strip-blue); }
  .card--front .film-hole { background: var(--frame-blue); }
  .front-identity {
    position: absolute; left: 52px; right: 52px; top: 0; bottom: 0;
    display: flex; flex-direction: column; align-items: center; justify-content: center;
    color: var(--paper); font-weight: 700;
  }
  .personal-mark {
    font-size: 88px; line-height: 1; letter-spacing: 4px;
  }
  .hospital-name {
    display: flex; align-items: center; gap: 12px;
    margin-top: 10px; font-size: 28px; letter-spacing: .5px;
  }
  .hospital-mark { width: 20px; height: 20px; background: var(--paper); }

  /* Back */
  .card--back { background: var(--paper); }
  .card--back .film-strip { background: var(--brand-blue); }
  .card--back .film-hole { background: var(--paper); }
  .contact {
    position: absolute; left: 52px; right: 52px; top: 0; bottom: 0;
    display: flex; flex-direction: column; align-items: center; justify-content: center;
    text-align: center; color: var(--ink-gray); font-size: 14px; line-height: 1.4;
  }
  .doctor-name { color: var(--brand-blue); font-size: 19px; line-height: 1.3; }
  .accent { color: var(--brand-blue); }
  .rule { width: 270px; height: 1px; background: var(--rule-gray); margin: 4px 0; }
  .rule--strong { background: var(--ink-gray); }
</style>
</head>
<body>
<main class="canvas">

  <section class="card card--back" aria-label="Reverso de la tarjeta">
    <div class="film-strip film-strip--left">
      <span class="film-hole"></span><span class="film-hole"></span><span class="film-hole"></span><span class="film-hole"></span>
    </div>
    <div class="contact">
      <p class="doctor-name">Dr. Mateo Anselmo Quiroga Benítez</p>
      <p class="specialty">Medicina general</p>
      <span class="rule rule--strong"></span>
      <p class="accent">HOSPITAL ALMENDRAL</p>
      <p>Calle Tomás Ibarrola #527 Col. Peñascal</p>
      <span class="rule"></span>
      <p>Tel 471-5836</p>
      <p>mateoqb@correoandino.net</p>
      <span class="rule"></span>
      <p><span class="accent">Sábado y domingo</span> 10:00 am a 10:00pm</p>
      <p><span class="accent">Emergencias:</span> 613-907-5148</p>
      <p class="accent">English Spoken</p>
    </div>
    <div class="film-strip film-strip--right">
      <span class="film-hole"></span><span class="film-hole"></span><span class="film-hole"></span><span class="film-hole"></span>
    </div>
  </section>

  <section class="card card--front" aria-label="Anverso de la tarjeta">
    <div class="film-strip film-strip--left">
      <span class="film-hole"></span><span class="film-hole"></span><span class="film-hole"></span><span class="film-hole"></span>
    </div>
    <div class="front-identity">
      <p class="personal-mark">MAQB</p>
      <p class="hospital-name"><span class="hospital-mark"></span><span>Hospital Almendral</span></p>
    </div>
    <div class="film-strip film-strip--right">
      <span class="film-hole"></span><span class="film-hole"></span><span class="film-hole"></span><span class="film-hole"></span>
    </div>
  </section>

</main>
</body>
</html>
```